Modern and strong website design for a Dutch crowdsourcing company
.

We are startup company providing crowdsourcing of administrative and customers service tasks for larger companies and other organizations. We offer cost savings and scale-ability combined with higher quality of execution. We will soon enter the market and need a website that has two major target groups: 1. Our corporate customers 2. The mainly younger crowd executing the tasks on our platform.
The target group of customers are Influencers and decision makers with companies and other organizations in with large administrative and customer service departments. Most information in the startup phase will be targeting this group.
The target group of future crowd workers will be heterogeneous, from students to stay at home mums or night shift workers who want to earn some extra money by performing easy to execute microtasks in the cloud. We will target both Dutch and international workers.

The website must be developed for browsing on a computer but also be optimized for mobile devices and tablets.
The website must be optimized and tested for the major browsers on windows, macOS and mobile devices.

For the minimum requirement for the website see attached wireframes

The present landing page http://bravolinkhive.com and logo are not reflecting our preferences!
See enclosed a new logo that stands for both the crowdwork (performed for our customers) and the crowd (a hive in motion).

Target Market(s)

see tekst above.

Industry/Entity Type

Business Service

Coding

Coded - Design and coding required

Number of Pages Required

5+ page

Font styles to use
Sans Serif
Other font styles liked:
• Lato, Open Sans

Colors

Designer to choose colors to be used in the design.

Requirements
Must have
• start devider screen
• home page displaying business and worker information
• a page displaying only info for businesses
• a page displaying only info for workers
• a contact form
• a reviews page
• color scheme from logo
• responsiveness!
Nice to have
• Nice animations
• overlapping blocks, animated on scroll
• lightbox effects if applicable
• animated mobile menu icon and menu itself

```html
<!DOCTYPE html>
<html lang="en">
<head>
<meta charset="utf-8">
<title>A Hive in Motion — Businesses and Workers</title>
<link href="https://fonts.googleapis.com/css2?family=Lato:wght@400;700;900&display=swap" rel="stylesheet">
<style>
  :root {
    --ink: #7a7a7d;
    --ink-soft: #8a8a8d;
    --slate: #7b7b7e;
    --orange: #f5821f;
    --white: #ffffff;
    --hero-dark: #2b2b2d;
    --hero-mid: #4a4644;
  }
  * { box-sizing: border-box; margin: 0; padding: 0; }
  html, body { width: 1200px; height: 1000px; overflow: hidden; background: var(--white); }
  body { position: relative; font-family: "Lato", sans-serif; color: var(--ink); }

  .hero-band {
    position: absolute; left: 0; top: 0; width: 1200px; height: 95px;
    background: linear-gradient(90deg, #3a3a3c 0%, #5a4a40 25%, #8a837c 50%, #3b3a38 75%, var(--hero-dark) 100%);
  }
  .scroll-cue { position: absolute; left: 585px; width: 30px; height: 14px; }
  .scroll-cue--hero { top: 42px; }
  .scroll-cue--section { top: 808px; }

  .section-title {
    position: absolute; font-size: 22px; font-weight: 900; letter-spacing: 4.5px; text-transform: uppercase;
  }
  .section-title--business { left: 234px; top: 187px; color: var(--slate); }
  .section-title--workers { left: 484px; top: 484px; color: var(--orange); }

  .section-copy { position: absolute; font-size: 10px; line-height: 17.5px; color: var(--ink-soft); }
  .section-copy p + p { margin-top: 17.5px; }
  .section-copy--business { left: 234px; top: 230px; width: 482px; }
  .section-copy--workers { left: 484px; top: 527px; width: 478px; }

  .cta {
    position: absolute; display: flex; align-items: center; justify-content: center;
    color: var(--white); font-size: 10px; font-weight: 700; text-transform: uppercase; letter-spacing: .2px;
  }
  .cta--business { left: 601px; top: 389px; width: 113px; height: 25px; background: var(--slate); border-radius: 13px 0 13px 13px; }
  .cta--workers { left: 485px; top: 688px; width: 106px; height: 25px; background: var(--orange); border-radius: 0 13px 13px 13px; box-shadow: 0 6px 14px rgba(245,130,31,.35); }

  .photo { position: absolute; width: 169px; height: 223px; }
  .photo--business {
    left: 797px; top: 192px; border-radius: 14px 14px 0 14px;
    background: linear-gradient(160deg, #b9a894 0%, #6b5544 40%, #3b3a40 70%, #8a6a4a 100%);
    box-shadow: 0 12px 24px rgba(0,0,0,.12);
  }
  .photo--workers {
    left: 235px; top: 490px; border-radius: 14px 0 14px 14px;
    background: linear-gradient(160deg, #7a5040 0%, #b9b4ae 45%, #5a4a44 75%, #2c2a2a 100%);
    box-shadow: 0 12px 24px rgba(245,130,31,.18);
  }
  .carousel-arrow { position: absolute; width: 10px; height: 24px; }
  .arrow-business-prev { left: 762px; top: 291px; }
  .arrow-business-next { left: 990px; top: 291px; }
  .arrow-workers-prev { left: 201px; top: 588px; }
  .arrow-workers-next { left: 429px; top: 588px; }

  .contact { position: absolute; left: 0; width: 1200px; text-align: center; font-size: 10px; letter-spacing: 2px; color: var(--ink); }
  .contact--email { top: 954px; }
  .contact--phone { top: 975px; }
</style>
</head>
<body>
  <header class="hero-band" role="img" aria-label="Photo of a desk with a phone and a coffee cup">
  </header>
  <svg class="scroll-cue scroll-cue--hero" viewBox="0 0 30 14"><polyline points="1,2 15,12 29,2" fill="none" stroke="#ffffff" stroke-width="1.3"/></svg>

  <section class="audience audience--business">
    <h2 class="section-title section-title--business">Businesses</h2>
    <div class="section-copy section-copy--business">
      <p>Lorem ipsum dolor sit amet, consectetuer adipiscing elit. Aenean commodo ligula eget dolor. Aenean massa. Cum sociis natoque penatibus et magnis dis parturient montes, nascetur ridiculus mus.Donec quam felis, ultricies nec, pellentesque eu, pretium quis, sem. Nulla consequat massa quis enim. Donec pede justo, fringilla vel, aliquet nec, vulputate eget, arcu.</p>
      <p>In enim justo, rhoncus ut, imperdiet a, venenatis vitae, justo. Nullam dictum felis eu pede mollis pretium. Integer tincidunt. Cras dapibus. Vivamus elementum semper nisi. Aenean vulputate eleifend tellus. Aenean leo ligula, porttitor eu, consequat vitae, eleifend ac, enim. Aliquam lorem ante, dapibus in, viverra quis, feugiat a,</p>
    </div>
    <a class="cta cta--business">For businesses</a>
    <svg class="carousel-arrow arrow-business-prev" viewBox="0 0 10 24"><polyline points="9,1 1,12 9,23" fill="none" stroke="#8a8a8d" stroke-width="1"/></svg>
    <div class="photo photo--business" role="img" aria-label="Photo of two business people shaking hands over coffee"></div>
    <svg class="carousel-arrow arrow-business-next" viewBox="0 0 10 24"><polyline points="1,1 9,12 1,23" fill="none" stroke="#8a8a8d" stroke-width="1"/></svg>
  </section>

  <section class="audience audience--workers">
    <svg class="carousel-arrow arrow-workers-prev" viewBox="0 0 10 24"><polyline points="9,1 1,12 9,23" fill="none" stroke="#8a8a8d" stroke-width="1"/></svg>
    <div class="photo photo--workers" role="img" aria-label="Photo of a young woman working with a pen"></div>
    <svg class="carousel-arrow arrow-workers-next" viewBox="0 0 10 24"><polyline points="1,1 9,12 1,23" fill="none" stroke="#f5821f" stroke-width="1"/></svg>
    <h2 class="section-title section-title--workers">Workers</h2>
    <div class="section-copy section-copy--workers">
      <p>Lorem ipsum dolor sit amet, consectetuer adipiscing elit. Aenean commodo ligula eget dolor. Aenean massa. Cum sociis natoque penatibus et magnis dis parturient montes, nascetur ridiculus mus.</p>
      <p>Donec quam felis, ultricies nec, pellentesque eu, pretium quis, sem. Nulla consequat massa quis enim. Donec pede justo, fringilla vel, aliquet nec, vulputate eget, arcu. In enim justo, rhoncus ut, imperdiet a, venenatis vitae, justo. Nullam dictum felis eu pede mollis pretium. Integer tincidunt. Cras dapibus. Vivamus elementum semper nisi. Aenean vulputate eleifend tellus. Aenean leo ligula, porttitor eu, consequat vitae, eleifend ac, enim. Aliquam lorem ante, dapibus in, viverra quis, feugiat a, tellus. Phasellus viverra nulla ut metus varius</p>
    </div>
    <a class="cta cta--workers">For workers</a>
  </section>

  <svg class="scroll-cue scroll-cue--section" viewBox="0 0 30 14"><polyline points="1,2 15,12 29,2" fill="none" stroke="#7a7a7d" stroke-width="1.2"/></svg>

  <footer>
    <p class="contact contact--email">info@bravolinkhive.com</p>
    <p class="contact contact--phone">0170 004 512</p>
  </footer>
</body>
</html>
```